Verdant Holdings SA Business Cards

Dear all,
Thank you for reading my brief and project. My company is doing doing advisory in real estate and to comapnies + real estates services as asset management, brokerage, development etc.
I would like to get a business card for my company which is clear, professionnal and serious.
Please have a look to the attachement to see the logos of the company

Industry/Entity Type

Real Estate

Contact Information for Business Card

I would like to have in the business card the following
Principal side:
- Logo of the company (or Monogram)
- First and Last Name (Marcel Tobler)
- Mobile number
- email address

Second side:
- Address (Chemin des Vergers 17, 1292 Chambésy - Switzerland)
- website (www.verdantholdings.ch)

Requirements
Must have
• Refer to the typeface and logo colors

```html
<!DOCTYPE html>
<html lang="en">
<head>
<meta charset="utf-8">
<title>Verdant Holdings SA – Business Cards</title>
<link href="https://fonts.googleapis.com/css2?family=Montserrat:wght@300;500;600&family=Lato:wght@400&display=swap" rel="stylesheet">
<style>
  :root {
    --stage: #1c1d1f;
    --navy: #2b3d50;
    --ink: #36404c;
    --blue: #1c7fcf;
    --paper: #ffffff;
    --rule: #5c6672;
  }
  * { margin: 0; padding: 0; box-sizing: border-box; }
  html, body { width: 1200px; height: 895px; overflow: hidden; background: var(--stage); }
  .canvas { position: relative; width: 1200px; height: 895px; }

  .card {
    position: absolute; left: 310px; width: 580px; height: 331px;
    box-shadow: 0 18px 40px rgba(0,0,0,.55);
  }
  .card--back { top: 88px; background: var(--navy); color: var(--paper); }
  .card--front { top: 474px; background: var(--paper); color: var(--ink); }

  .brand { position: absolute; display: flex; align-items: center; gap: 22px; }
  .brand__mark { width: 46px; height: 46px; }
  .brand__divider { width: 1px; height: 74px; }
  .brand__name {
    font-family: "Montserrat", sans-serif; font-weight: 500;
    font-size: 21px; letter-spacing: 1px; text-transform: uppercase; white-space: nowrap;
  }

  .card--back .brand { left: 150px; top: 110px; }
  .card--back .brand__mark { background: var(--paper); }
  .card--back .brand__divider { background: rgba(255,255,255,.45); }
  .card--back .website {
    position: absolute; left: 0; right: 0; top: 252px; text-align: center;
    font-family: "Lato", sans-serif; font-size: 13px; letter-spacing: 1.2px;
  }

  .card--front .brand { left: 38px; top: 42px; }
  .card--front .brand__mark { background: var(--blue); }
  .card--front .brand__divider { background: var(--blue); }

  .person { position: absolute; right: 36px; top: 150px; text-align: right; }
  .person__name {
    font-family: "Montserrat", sans-serif; font-size: 22px; text-transform: uppercase; letter-spacing: .5px;
  }
  .person__first { font-weight: 600; color: var(--ink); }
  .person__last { font-weight: 300; color: var(--blue); }
  .person__title { font-family: "Lato", sans-serif; font-size: 13px; margin-top: 2px; }

  .rule { position: absolute; left: 38px; right: 36px; top: 213px; height: 1px; background: var(--rule); }

  .contact { position: absolute; left: 38px; top: 232px; list-style: none; }
  .contact li {
    display: flex; align-items: center; gap: 10px;
    font-family: "Lato", sans-serif; font-size: 13.5px; line-height: 24px; letter-spacing: .4px;
  }
  .contact svg { width: 13px; height: 13px; fill: none; stroke: var(--blue); stroke-width: 1.6; }

  .address {
    position: absolute; right: 36px; top: 232px; text-align: right;
    font-family: "Lato", sans-serif; font-size: 13.5px; line-height: 21px; letter-spacing: .4px; font-style: normal;
  }
</style>
</head>
<body>
<main class="canvas">

  <section class="card card--back" aria-label="Business card, back">
    <div class="brand">
      <span class="brand__mark"></span>
      <span class="brand__divider"></span>
      <span class="brand__name">Verdant Holdings</span>
    </div>
    <p class="website">www.verdantholdings.ch</p>
  </section>

  <section class="card card--front" aria-label="Business card, front">
    <div class="brand">
      <span class="brand__mark"></span>
      <span class="brand__divider"></span>
      <span class="brand__name">Verdant Holdings</span>
    </div>

    <div class="person">
      <p class="person__name"><span class="person__first">Marcel</span> <span class="person__last">Tobler</span></p>
      <p class="person__title">Founder &amp; CEO</p>
    </div>

    <div class="rule"></div>

    <ul class="contact">
      <li>
        <svg viewBox="0 0 16 16" aria-hidden="true"><path d="M4 1.5l2.5 3-1.5 1.8a9 9 0 0 0 4.7 4.7l1.8-1.5 3 2.5-1.6 2.2C8 14 2 8 1.8 3.1z"/></svg>
        000 000 0000
      </li>
      <li>
        <svg viewBox="0 0 16 16" aria-hidden="true"><rect x="1.5" y="3.5" width="13" height="9"/><path d="M1.5 3.5L8 9l6.5-5.5"/></svg>
        marcel_t@verdantholdings.ch
      </li>
      <li>
        <svg viewBox="0 0 16 16" aria-hidden="true"><circle cx="8" cy="8" r="6.5"/><path d="M1.5 8h13M8 1.5c-3 3.5-3 9.5 0 13M8 1.5c3 3.5 3 9.5 0 13"/></svg>
        www.verdantholdings.ch
      </li>
    </ul>

    <address class="address">
      Chemin des Vergers 17<br>
      1292 Chambésy<br>
      Switzerland
    </address>
  </section>

</main>
</body>
</html>
```